KRT Flyer - Workshop and Scholarship Program

KRT needs a double sided flyer designed for an upcoming workshop we have that is also doubling as a launch of our business and of our scholarship program.
All of the information required to go onto the flyer is contained below in the two documents.
The first is a word document that contains the details to be included on the flyer - this is in the order that I wish to present them also.
The second document is an earlier example of a winning flyer that was designed for an earlier launch. I was happy with many of the characteristics within this flyer including the photo/bio at the bottom.
Please note that the language and descriptions have all changed.
Please use images and patterns that you feel address the requirements of the advertisement.
I have included the original design files for the logo and flyer to get the logo and bio image
Target Market(s)
HSC students (Final Year of High School
Industry/Entity Type
Education
Font styles to use
Other font styles liked:
- Myriad Pro
Requirements
Must have
- The logo of the business must be shown a maximum of twice on both sides. Please remove the surrounding square and imbed it into the flyer.
- A simple but effective design
Nice to have
- Images that reflect the content
Should not have
- Too much going on that the message is lost.

```html
<!DOCTYPE html>
<html lang="en">
<head>
<meta charset="utf-8">
<title>KRT Flyer – HSC Workshop and Scholarship Offer</title>
<link rel="stylesheet" href="https://fonts.googleapis.com/css2?family=Oswald:wght@500;600&family=Source+Sans+3:wght@400;600;700;800&display=swap">
<style>
  :root {
    --orange: #f47b20;
    --orange-deep: #e0660f;
    --black: #1e1e1e;
    --charcoal: #2b2b2b;
    --grey-panel: #e6e6e6;
    --grey-strip: #ededed;
    --grey-label: #9a9a9a;
    --text: #3a3a3a;
    --white: #ffffff;
    --backdrop: #dcdcdc;
  }
  * { box-sizing: border-box; margin: 0; padding: 0; }
  html, body {
    width: 1200px; height: 900px; overflow: hidden;
    background: var(--backdrop);
    font-family: "Source Sans 3", "Myriad Pro", sans-serif;
    color: var(--text);
  }
  .flyer {
    position: absolute; left: 296px; top: 20px;
    width: 608px; height: 860px;
    background: var(--white);
    overflow: hidden;
    box-shadow: 0 6px 24px rgba(0,0,0,.18);
  }
  .hero-photo {
    position: absolute; left: 0; top: 0; width: 608px; height: 320px;
    background:
      radial-gradient(ellipse at 70% 45%, #d9b08c 0%, rgba(217,176,140,0) 45%),
      linear-gradient(180deg, #f4f7ef 0%, #c9dcae 40%, #7fae4a 72%, #5d8f2f 100%);
  }
  .brand {
    position: absolute; left: 18px; top: 16px;
    display: flex; align-items: center; gap: 8px;
    background: var(--white); padding: 8px 14px 8px 10px; border-radius: 4px;
  }
  .brand-dot { width: 30px; height: 30px; border-radius: 50%; background: var(--orange); }
  .brand-name { font-weight: 800; font-size: 30px; color: var(--charcoal); line-height: 1; letter-spacing: .5px; }

  .title-banner {
    position: absolute; left: 0; top: 286px; width: 380px; height: 112px;
    background: var(--orange); color: var(--white);
    padding: 12px 0 0 28px;
  }
  .title-year { font-weight: 800; font-size: 40px; line-height: 1; letter-spacing: .5px; }
  .title-sub {
    font-family: "Oswald", sans-serif; font-weight: 500;
    font-size: 19px; line-height: 1.12; margin-top: 6px; text-transform: uppercase;
  }
  .callout {
    position: absolute; left: 340px; top: 322px; width: 268px; height: 96px;
    background: var(--black);
    clip-path: polygon(14% 0, 100% 0, 100% 100%, 0 100%);
    padding: 12px 14px 0 48px; text-align: center;
  }
  .callout-lead { color: var(--orange); font-weight: 700; font-size: 11px; }
  .callout-main { color: var(--white); font-size: 17px; line-height: 1.05; }
  .callout-lead + .callout-main { margin-bottom: 4px; }

  .details { position: absolute; left: 28px; top: 412px; width: 272px; font-size: 9.5px; line-height: 1.3; }
  .section-heading { color: var(--orange); font-weight: 700; font-size: 12px; margin-bottom: 4px; }
  .bullets { display: grid; grid-template-columns: 1fr 1fr; gap: 0 10px; margin-bottom: 8px; }
  .bullets ul { list-style: none; }
  .bullets li { padding-left: 8px; position: relative; margin-bottom: 3px; }
  .bullets li::before { content: ""; position: absolute; left: 0; top: 5px; width: 4px; height: 4px; background: var(--orange); }
  .details p { margin-bottom: 8px; }
  .details .confirm-note {
    margin: 0 -8px 0 -28px; padding: 5px 8px 5px 28px;
    background: var(--grey-strip);
  }

  .sessions {
    position: absolute; left: 308px; top: 418px; width: 280px; height: 300px;
    background: var(--grey-panel); padding: 8px 14px;
  }
  .session-title { text-align: center; font-weight: 700; font-size: 15px; color: var(--black); margin: 2px 0 6px; }
  .session-table { width: 100%; border-collapse: separate; border-spacing: 0 4px; font-size: 8.5px; }
  .session-table th {
    width: 86px; text-align: left; font-weight: 600; color: var(--white);
    padding: 4px 8px; vertical-align: top;
  }
  .session-table td { padding: 2px 8px; line-height: 1.25; color: var(--text); }
  .session-one th { background: var(--orange); }
  .session-two th { background: var(--grey-label); }

  .footer-accent {
    position: absolute; left: 0; top: 718px; width: 178px; height: 108px;
    background: linear-gradient(180deg, var(--orange) 0%, var(--orange-deep) 100%);
  }
  .bio-photo {
    position: absolute; left: 28px; top: 642px; width: 150px; height: 124px;
    border: 4px solid var(--orange);
    background: linear-gradient(160deg, #c9d4dc 0%, #8fa3b3 55%, #5b7890 100%);
  }
  .bio-name { position: absolute; left: 190px; top: 724px; font-size: 10px; line-height: 1.3; color: var(--black); }
  .bio-name strong { display: block; font-size: 11px; }

  .footer-text {
    position: absolute; left: 190px; top: 776px; width: 390px;
    font-size: 8.5px; line-height: 1.35; color: var(--text);
  }
  .footer-band {
    position: absolute; left: 0; bottom: 0; width: 608px; height: 30px;
    background: linear-gradient(90deg, var(--black), #3a3a3a);
  }
  .footer-stripe { position: absolute; left: 0; bottom: 30px; width: 608px; height: 4px; background: var(--orange); }
</style>
</head>
<body>
  <article class="flyer">
    <div class="hero-photo" role="img" aria-label="Photo of three smiling teenage students lying on the grass looking at a pink tablet"></div>

    <div class="brand">
      <span class="brand-dot"></span>
      <span class="brand-name">KRT</span>
    </div>

    <header class="title-banner">
      <div class="title-year">2017 FREE</div>
      <div class="title-sub">HSC Preparation Workshop<br>and Scholarship Offer</div>
    </header>

    <aside class="callout">
      <div class="callout-lead">Limited spots available at both</div>
      <div class="callout-main">venues! Don't miss out!</div>
      <div class="callout-lead">This event could make all the difference</div>
      <div class="callout-main">To your HSC Experience!</div>
    </aside>

    <section class="details">
      <h2 class="section-heading">What will the day involve?</h2>
      <div class="bullets">
        <ul>
          <li>Goal setting and study skills for the year</li>
          <li>Exam techniques to improve your HSC results</li>
          <li>Managing stress and staying motivated</li>
        </ul>
        <ul>
          <li>A scholarship information session with our team</li>
          <li>Tips on choosing your subjects and courses</li>
          <li>Free study planner for every student attending</li>
        </ul>
      </div>
      <p>Places are strictly limited so register early to secure a spot for you and a parent.</p>
      <h2 class="section-heading">How to register:</h2>
      <p>Email your name, school and chosen venue to the address below.</p>
      <p class="confirm-note">You will then be sent confirming further details.</p>
    </section>

    <section class="sessions">
      <h3 class="session-title">Presentation 1</h3>
      <table class="session-table session-one">
        <tr><th>Date</th><td>Saturday 14 October 2017</td></tr>
        <tr><th>Location</th><td>Parramatta</td></tr>
        <tr><th>Time</th><td>Session 1: 9.00 – 12.00<br>Session 2: 1.00 – 4.00</td></tr>
        <tr><th>Cost</th><td>$0 – Free for all HSC students</td></tr>
      </table>
      <h3 class="session-title">Presentation 2</h3>
      <table class="session-table session-two">
        <tr><th>Date</th><td>Sunday 15 October 2017</td></tr>
        <tr><th>Location</th><td>Chatswood</td></tr>
        <tr><th>Time</th><td>Session 1: 9.00 – 12.00<br>Session 2: 1.00 – 4.00</td></tr>
        <tr><th>Cost</th><td>$0 – Free for all HSC students</td></tr>
      </table>
    </section>

    <div class="footer-accent"></div>
    <div class="bio-photo" role="img" aria-label="Portrait photo of the workshop presenter, Mark Dalton"></div>
    <div class="bio-name"><strong>Mark Dalton</strong>Keys Reach Thrive owner</div>

    <p class="footer-text">Mark is a former teacher and HSC marker with over fifteen years of experience. KRT was founded to help students plan, study and succeed in their final year, with a scholarship program open to all.</p>

    <div class="footer-stripe"></div>
    <div class="footer-band"></div>
  </article>
</body>
</html>
```